Craft oriented film company needs a Business Card design

Hi all,
We're a 2-man band film company in New Zealand called Kestrel Pictures. We're good honest blokes, who are very passionate about the craft of film making. I've attached our current logo which has a bit of a crafty/artisan feel that we like. Feel free to use it - or throw the baby out with the bathwater and start again..... you never know, you might inspire a complete brand re-work.

In any case, the vibe we want to give out is that we are solid, dependable and no bullshit - but without compromising creative excellence and being in the now. We like the 'Brooklyn' artisan style of work.

Preferably single sided.

We need the standard stuff:
Name, job title, cellphone, email address and physical address (this can be smaller if you like - street, suburb, city & zip, country [if you want])

Check out our website to learn more about us: kestrelpictures.example

Target Market(s)

Brand marketers and advertising agency creatives looking for video production.

Industry/Entity Type

Baby

Requirements
Should not have
• Nothing flashy or too 'futuristic', we want it to feel grounded and real. A limited colour palette is preferred.
We don't want any film reels or cameras or anything obvious like that.

```html
<!DOCTYPE html>
<html lang="en">
<head>
<meta charset="utf-8">
<title>Kestrel Pictures – Business Cards</title>
<link rel="stylesheet" href="https://fonts.googleapis.com/css2?family=Open+Sans:wght@400;600;700&display=swap">
<style>
  :root {
    --brand-orange: #dd8c2e;
    --cream: #fbeee0;
    --ink: #333333;
    --rule: #111111;
    --trim: #555555;
    --paper: #ffffff;
  }
  html, body {
    margin: 0;
    padding: 0;
    overflow: hidden;
    background: var(--paper);
  }
  .sheet {
    position: relative;
    width: 930px;
    height: 1200px;
    overflow: hidden;
    background: var(--paper);
    font-family: "Open Sans", Arial, sans-serif;
  }
  address { font-style: normal; }
  .card {
    position: absolute;
    left: 0;
    width: 930px;
    height: 520px;
  }
  .card--producer { top: 0; }
  .card--director { top: 670px; left: 2px; }
  .card__shapes {
    position: absolute;
    inset: 0;
  }
  .brand {
    position: absolute;
    left: 86px;
    top: 76px;
    color: var(--cream);
    font-weight: 700;
    line-height: 1;
  }
  .brand__word {
    display: block;
    font-size: 46px;
    letter-spacing: 1px;
  }
  .brand__sub {
    display: block;
    font-size: 26px;
    margin-top: 10px;
    margin-left: 40px;
  }
  .person {
    position: absolute;
    left: 557px;
    width: 320px;
    top: 82px;
    text-align: center;
    color: var(--cream);
    line-height: 1;
  }
  .person__name {
    display: block;
    font-size: 42px;
    font-weight: 600;
  }
  .person__role {
    display: block;
    font-size: 26px;
    font-weight: 400;
    margin-top: 4px;
  }
  .contact {
    position: absolute;
    left: 86px;
    top: 346px;
    margin: 0;
    color: var(--ink);
    font-size: 22px;
    line-height: 26.5px;
  }
  .contact span { display: block; white-space: nowrap; }
  .divider {
    position: absolute;
    left: 490px;
    top: 319px;
    width: 2px;
    height: 152px;
    background: var(--rule);
  }
  .studio {
    position: absolute;
    left: 578px;
    top: 370px;
    margin: 0;
    color: var(--ink);
  }
  .studio__web {
    display: block;
    font-size: 22px;
    line-height: 28px;
  }
  .studio__address {
    display: block;
    font-size: 17px;
    line-height: 21px;
    margin-top: 2px;
  }
</style>
</head>
<body>
<main class="sheet">

  <article class="card card--producer">
    <svg class="card__shapes" width="930" height="520" viewBox="0 0 930 520" aria-hidden="true">
      <polygon fill="var(--brand-orange)" points="3,3 929,3 929,268 792,307 642,268 3,268"/>
      <rect x="31" y="34" width="864" height="464" fill="none" stroke="var(--trim)" stroke-width="1"/>
    </svg>
    <div class="brand">
      <span class="brand__word">KESTREL</span>
      <span class="brand__sub">Pictures</span>
    </div>
    <div class="person">
      <span class="person__name">Rowan Ashby</span>
      <span class="person__role">Producer</span>
    </div>
    <address class="contact">
      <span>(64) 21-555-018</span>
      <span>rowan@kestrelpictures.example</span>
      <span>Arts &amp; Entertainment</span>
      <span>Broadcasting &amp; Media Production</span>
    </address>
    <div class="divider"></div>
    <address class="studio">
      <span class="studio__web">kestrelpictures.example</span>
      <span class="studio__address">12 Kauri st, mount eden,<br>auckland, new zealand 1024</span>
    </address>
  </article>

  <article class="card card--director">
    <svg class="card__shapes" width="930" height="520" viewBox="0 0 930 520" aria-hidden="true">
      <polygon fill="var(--brand-orange)" points="3,4 929,4 929,268 792,307 642,268 3,268"/>
      <rect x="32" y="34" width="866" height="465" fill="none" stroke="var(--trim)" stroke-width="1"/>
    </svg>
    <div class="brand">
      <span class="brand__word">KESTREL</span>
      <span class="brand__sub">Pictures</span>
    </div>
    <div class="person">
      <span class="person__name">Niall Fenwick</span>
      <span class="person__role">Director</span>
    </div>
    <address class="contact">
      <span>(64) 21-555-042</span>
      <span>niall@kestrelpictures.example</span>
      <span>Arts &amp; Entertainment</span>
      <span>Broadcasting &amp; Media Production</span>
    </address>
    <div class="divider"></div>
    <address class="studio">
      <span class="studio__web">kestrelpictures.example</span>
      <span class="studio__address">12 Kauri st, mount eden,<br>auckland, new zealand 1024</span>
    </address>
  </article>

</main>
</body>
</html>
```